Investment Management Firm Power point template

Harrowgate Capital is a real estate investment firm focused on buying commercial office and residential property in the UK. We produce powerpoint presentations for our Board of Directors, Investment Committee and also to external investors.

We are looking for a powerpoint design template which we can use for future presentations which provide a professional look and feel.

Our current website: http://www.harrowgatecapital.co.uk/

Target Market(s)

Institution Investors, Board of Directors, Professionals

Industry/Entity Type

Real Estate

Requirements
Must have
• Leverage off the current logo and colour scheme. However, does not have to purely rely on this colour scheme.
• - Title page
• - Content Page
• - Slide where graphs can be incorporated
• - Slide where photos can be incorporated
• - Slide of UK Map which can show where the property portfolio is currently located
• - Other slides incorporating smart art or other designs that can be used for future presentations
Nice to have
• An example of graphics that we would love to have in the powerpoint pack which we can easily edit has been attached

```html
<!DOCTYPE html>
<html lang="en">
<head>
<meta charset="utf-8">
<title>Harrowgate Capital – Presentation Template</title>
<link href="https://fonts.googleapis.com/css2?family=Arimo:wght@400;500;700&display=swap" rel="stylesheet">
<style>
:root{
  --navy:#34587a;
  --navy-dark:#2f4a62;
  --table-head:#3f5568;
  --sky:#7fadd1;
  --cyan:#29a9e0;
  --orange:#e0622a;
  --beige:#ede5dc;
  --gold:#9a7a3c;
  --paper:#f2f2f2;
  --white:#ffffff;
  --ink:#2c3e50;
}
*{margin:0;padding:0;box-sizing:border-box}
html,body{width:1200px;height:900px;overflow:hidden;background:var(--white)}
body{position:relative;font-family:"Arimo",Arial,sans-serif;color:var(--ink)}
.slide{position:absolute;width:512px;height:384px;overflow:hidden;box-shadow:4px 5px 9px rgba(0,0,0,.38)}
.slide--title{left:80px;top:62px;background:var(--navy)}
.slide--content{left:626px;top:62px;background:var(--paper)}
.slide--chart{left:80px;top:474px;background:var(--white)}
.slide--snapshot{left:626px;top:474px;background:var(--navy)}

.wordmark{display:flex;align-items:center;gap:7px;color:var(--navy-dark);font-weight:500;white-space:nowrap}
.wordmark__square{display:block;background:var(--navy-dark);flex:none}

/* title slide */
.title-logo{position:absolute;left:40px;top:79px;width:253px;height:52px;background:var(--white);padding-left:10px;font-size:23px;gap:8px}
.title-logo .wordmark__square{width:30px;height:30px}
.title-box{position:absolute;left:301px;top:79px;width:211px;height:52px;background:var(--sky);color:var(--white);padding:10px 14px;font-weight:700}
.title-box__main{font-size:20px;line-height:20px}
.title-box__sub{font-size:13px;line-height:15px}
.title-strip{position:absolute;left:0;top:359px;width:295px;height:9px;background:var(--sky)}
.title-date{position:absolute;left:315px;top:359px;color:var(--white);font-size:10px;font-weight:700}

/* content slide */
.content-photo{position:absolute;left:0;top:0;width:248px;height:340px;background:linear-gradient(160deg,#dfe5e8 0%,#aeb9be 45%,#6c7479 75%,#b9c2c6 100%)}
.content-footer{position:absolute;left:0;top:340px;width:248px;height:34px;background:var(--white);padding:0 0 0 22px;font-size:14px}
.content-footer .wordmark__square{width:17px;height:17px}
.content-text{position:absolute;left:264px;top:34px;width:218px}
.subtitle{color:var(--orange);font-size:10.5px;font-weight:700}
.slide-title{color:var(--navy-dark);font-size:12px;font-weight:700;letter-spacing:.3px}
.content-text p{margin-top:13px;font-size:9.4px;line-height:11px;font-weight:700;color:#3e5064;hyphens:auto}
.content-text p + p{margin-top:11px}
.bullets{list-style:none;margin-top:11px;font-size:9.4px;font-weight:700;color:#3e5064}
.bullets li{position:relative;padding-left:18px;margin-bottom:12px}
.bullets li::before{content:"";position:absolute;left:2px;top:3px;width:4px;height:4px;border-radius:50%;background:var(--orange)}

/* chart slide */
.chart-heading{position:absolute;left:241px;top:24px;height:40px;border-left:3px solid var(--cyan);padding:11px 0 0 21px}
.chart-heading sup{font-size:6px}
.data-table{position:absolute;left:38px;top:105px;width:435px;border-collapse:collapse;font-size:8.5px;text-align:center}
.data-table th{background:var(--table-head);color:var(--white);font-weight:700;height:34px;border:2px solid var(--white);line-height:9px;padding:0 4px}
.data-table td{background:var(--beige);height:30px;border:2px solid var(--white);color:#222;line-height:10px}
.data-table sup{font-size:5px}
.data-table .row-total td{color:var(--gold)}
.chart-logo{position:absolute;left:20px;top:349px;font-size:14px}
.chart-logo .wordmark__square{width:17px;height:17px}
.endnotes{position:absolute;left:247px;top:342px;width:265px;height:30px;background:var(--table-head);color:var(--white);font-size:6px;font-weight:700;display:grid;grid-template-columns:1fr 1fr;padding:5px 14px;row-gap:6px}

/* snapshot slide */
.snapshot-heading{position:absolute;left:84px;top:20px;color:var(--white);font-weight:700;font-size:10px;letter-spacing:.2px}
.snapshot-heading small{font-size:6.5px;margin-left:3px}
.snapshot-panel{position:absolute;left:84px;top:38px;width:349px;height:285px;background:var(--white)}
.snapshot-footer{position:absolute;left:0;top:342px;width:512px;height:33px;background:var(--white);padding:0 0 0 22px;font-size:14px}
.snapshot-footer .wordmark__square{width:17px;height:17px}
</style>
</head>
<body>

<section class="slide slide--title">
  <div class="title-logo wordmark"><span class="wordmark__square"></span>Harrowgate Capital</div>
  <div class="title-box">
    <div class="title-box__main">TITLE</div>
    <div class="title-box__sub">SUBTITLE</div>
  </div>
  <div class="title-strip"></div>
  <div class="title-date">TEXT OR DATE</div>
</section>

<section class="slide slide--content">
  <div class="content-photo" role="img" aria-label="Aerial photograph of an open-cut landscape with winding terraces"></div>
  <div class="content-footer wordmark"><span class="wordmark__square"></span>Harrowgate Capital</div>
  <div class="content-text" lang="en">
    <div class="subtitle">SubTitle</div>
    <div class="slide-title">SLIDE TITLE</div>
    <p>Lorem ipsum dolor sit amet, quo sapientem in&shy;ciderint ne, ad dicta probatus prodesset pri. His harum omnesque tractatos ex. Fugit nominati nam ea, no maiorum voluptua accusamus cum. An admodum phaedrum con&shy;clusionemque sit, dolor philosophia ut duo. Ei sit ipsum accommodare. Vel nibh laoreet sa&shy;lutandi ut, ius vocibus honestatis consequuntur no.</p>
    <p>In sit falli causae. Mundi tation ut quo.<br>Ex usu modo corrumpit consequat, ei facilis quaestio vim, ea aperiam euripidis eum. Ne quas mucius quaerendum duo, amet partiendo intellegam eum at. Mei velit novum pericula in, nostrud theophrastus cum ei.</p>
    <ul class="bullets"><li>Bullets</li><li>Sub-bullets</li><li>Sub-bullets</li></ul>
  </div>
</section>

<section class="slide slide--chart">
  <div class="chart-heading">
    <div class="subtitle">SubTitle</div>
    <div class="slide-title">CHART EXAMPLE <sup>(01)</sup></div>
  </div>
  <table class="data-table">
    <colgroup><col style="width:90px"><col style="width:113px"><col style="width:70px"><col style="width:162px"></colgroup>
    <tr><th>Region</th><th>Gold Production(2)<br>(000 oz. Au eq.)</th><th>% of Total<br>Production</th><th>Production cost of Sales(3)<br>($/oz. Au eq.)</th></tr>
    <tr><td>South America</td><td>xxx – xxx</td><td>xx%</td><td>$xxx– $xxx</td></tr>
    <tr><td>North America</td><td>xxx – xxx</td><td>xx%</td><td>$xxx – $xxx</td></tr>
    <tr><td>West Africa<sup>(2)</sup><br>(attributable)</td><td>xxx – xxx</td><td>xx%</td><td>$xxx – $xxx</td></tr>
    <tr><td>Russia</td><td>xxx – xxx</td><td>xx%</td><td>$xxx – $xxx</td></tr>
    <tr class="row-total"><td>Total Aldermoor<sup>(2)</sup>:</td><td>xx – xx million</td><td>xx%</td><td>Gold equivalent: $xxx –$xxx/oz<br>By-product: $xxx – $xxx/oz</td></tr>
  </table>
  <div class="chart-logo wordmark"><span class="wordmark__square"></span>Harrowgate Capital</div>
  <div class="endnotes">
    <span>(01) Endnote example</span><span>(03) Endnote example</span>
    <span>(02) Endnote example</span><span>(04) Endnote example</span>
  </div>
</section>

<section class="slide slide--snapshot">
  <div class="snapshot-heading">MARKET SNAPSHOT<small>SPECULATIVE DEVELOPMENT - TOP 10 MARKETS</small></div>
  <div class="snapshot-panel">
    <svg width="349" height="285" viewBox="0 0 349 285" font-family="Arimo, Arial, sans-serif">
      <defs>
        <linearGradient id="crane-tone" x1="0" y1="0" x2="0" y2="1">
          <stop offset="0" stop-color="#e4e6e8"/><stop offset="1" stop-color="#f3f4f5"/>
        </linearGradient>
        <linearGradient id="badge-tone" x1="0" y1="0" x2="1" y2="0">
          <stop offset="0" stop-color="#2a2a2a"/><stop offset="1" stop-color="#3a3a3a"/>
        </linearGradient>
      </defs>
      <g role="img" aria-label="Tower crane illustration behind the chart">
        <rect x="0" y="12" width="330" height="18" fill="url(#crane-tone)"/>
        <rect x="80" y="0" width="28" height="210" fill="url(#crane-tone)"/>
      </g>
      <text x="103" y="22" font-size="6" fill="#333">2%</text>
      <text x="170" y="22" font-size="5" fill="#333">% OF STOCK</text>
      <text x="306" y="22" font-size="6" fill="#333">5%</text>
      <line x1="100" y1="26" x2="316" y2="26" stroke="#29a9e0" stroke-width="1"/>
      <path d="M316 23 L321 26 L316 29 Z" fill="#29a9e0"/>
      <line x1="60" y1="75" x2="330" y2="75" stroke="#999" stroke-width=".5"/>
      <line x1="60" y1="162" x2="330" y2="162" stroke="#999" stroke-width=".5"/>
      <text x="52" y="77" font-size="5" fill="#333">0</text>
      <text x="52" y="164" font-size="5" fill="#333">3</text>
      <text x="28" y="120" font-size="5" fill="#333">m sq ft</text>
      <g fill="#29a9e0">
        <rect x="106" y="75" width="18" height="14"/>
        <rect x="128" y="75" width="18" height="12"/>
        <rect x="150" y="75" width="18" height="26"/>
        <rect x="172" y="75" width="18" height="9"/>
        <rect x="194" y="75" width="18" height="6"/>
        <rect x="216" y="75" width="18" height="9"/>
        <rect x="238" y="75" width="18" height="67"/>
        <rect x="260" y="75" width="18" height="75"/>
        <rect x="282" y="75" width="18" height="12"/>
        <rect x="304" y="75" width="18" height="6"/>
      </g>
      <g fill="#29a9e0" font-size="7" font-weight="700" text-anchor="middle">
        <text x="115" y="97">0.5m</text><text x="137" y="95">0.4m</text>
        <text x="159" y="109">0.9m</text><text x="181" y="92">0.3m</text>
        <text x="203" y="89">0.2m</text><text x="225" y="92">0.3m</text>
        <text x="247" y="150">2.3m</text><text x="269" y="158">2.6m</text>
        <text x="291" y="95">0.4m</text><text x="313" y="89">0.2m</text>
      </g>
      <g fill="#111" font-size="4.5" font-weight="700">
        <text transform="translate(113,101) rotate(90)">EDINBURGH</text>
        <text transform="translate(135,99) rotate(90)">GLASGOW</text>
        <text transform="translate(157,113) rotate(90)">MANCHESTER</text>
        <text transform="translate(179,96) rotate(90)">MIDTOWN</text>
        <text transform="translate(201,93) rotate(90)">UXBRIDGE</text>
        <text transform="translate(223,96) rotate(90)">CAMBRIDGE</text>
        <text transform="translate(245,154) rotate(90)">CITY</text>
        <text transform="translate(267,162) rotate(90)">WEST END</text>
        <text transform="translate(289,99) rotate(90)">READING</text>
        <text transform="translate(311,93) rotate(90)">STAINES</text>
      </g>
      <text x="174" y="203" font-size="5.5" font-weight="700" fill="#d8232a" text-anchor="middle">2014 TOTAL RETURNS (% PA)</text>
      <rect x="24" y="212" width="316" height="72" rx="4" fill="url(#badge-tone)" role="img"
            aria-label="Four pound-sign badges showing 2014 total returns: Rest of the UK 16.9%, City 20.2%, South East 22.5%, West End and Midtown 24.0%"/>
    </svg>
  </div>
  <div class="snapshot-footer wordmark"><span class="wordmark__square"></span>Harrowgate Capital</div>
</section>

</body>
</html>
```